Book cover - Quiet Rooms, Open Doors

Book cover for Ebook (Pagelight) and wrap around print cover (Printvale) (back, front, and spine)

The book title (may slightly change by end of brief):
(MAIN TITLE) 'Quiet Rooms, Open Doors'
(SUB HEADING) 'A Week-by-Week Practical Workbook to Loosen Nervous Habits, Quieten Doubt and Build Steady Poise'
by Dr Owen Hartley

I would like a bold, stand out cover. Contemporary. I would like to avoid stereotypical images of people looking anxious or worried. I would like the design to be more uplifting and hopeful, rather than focusing on the negative aspect of anxiety, but avoiding cliched photos of people raising their hands in the air, smiling and jumping etc. The cover should appeal to both men and women.

Trim size of book cover (for PrintVale) is 5.25" x 8" back and front with a spine size of 0.477 inches

Reason: I have decided to extend the deadline by 1 more day, not because I am unhappy with the quality of the designs, but because a few designers have contacted me to explain they have had technical difficulties when submitting their files. Thanks everyone for the hard work and great designs.

Target Market(s)

Males and females (16+) who struggle with social anxiety and shyness

Industry/Entity Type

Social

Font styles to use
Serif

Requirements
Must have
• Bold cover that is modern and contemporary. For example, I like these covers:
• http://shrtlnk.example/k4Tq9Zb
• http://shrtlnk.example/m8Wv2Hn
• http://shrtlnk.example/p3Jx6Lr
• http://shrtlnk.example/t7Gd1Qe
• http://shrtlnk.example/v2Nk8Fy
• http://shrtlnk.example/w9Bh4Cs
• http://shrtlnk.example/z5Mf3Ud
Nice to have
• Open to abstract designs.
Should not have
• No stereotypical pictures of people who look anxious or worried. Avoid cliched photos of people raising their hands in the air, smiling and jumping etc.

```html
<!DOCTYPE html>
<html lang="en">
<head>
<meta charset="utf-8">
<title>Quiet Rooms, Open Doors — Dr Owen Hartley</title>
<link rel="stylesheet" href="https://fonts.googleapis.com/css2?family=Jost:wght@300;400;500;800&display=swap">
<style>
  :root {
    --paper: #ffffff;
    --ink: #111111;
    --accent-red: #a3161b;
    --rule: #c9a48a;
    --tone-warm: #f5a14a;
    --tone-sun: #f6dd5a;
    --tone-cool: #8fb7e0;
    --tone-violet: #b46ad6;
  }
  * { margin: 0; padding: 0; box-sizing: border-box; }
  html, body {
    width: 1200px; height: 900px; overflow: hidden;
    background: var(--paper);
    font-family: "Jost", "Futura", sans-serif;
    color: var(--ink);
  }
  .cover {
    position: relative;
    width: 1200px; height: 900px;
    background: var(--paper);
  }
  .rule {
    position: absolute;
    left: 305px; width: 620px; height: 1px;
    background: linear-gradient(90deg, transparent, var(--rule) 20%, var(--rule) 80%, transparent);
  }
  .rule--top-a { top: 32px; }
  .rule--top-b { top: 103px; }
  .rule--bottom-a { top: 805px; left: 310px; width: 600px; }
  .rule--bottom-b { top: 853px; left: 310px; width: 600px; }

  .subtitle {
    position: absolute;
    top: 41px; left: 310px; width: 610px;
    text-align: center;
    font-size: 19px; font-weight: 400; line-height: 1.22;
    text-wrap: balance;
  }

  .artwork {
    position: absolute;
    left: 305px; top: 135px; width: 620px; height: 665px;
    border-radius: 60px;
    background: linear-gradient(160deg, var(--tone-warm) 0%, var(--tone-sun) 38%, var(--tone-cool) 68%, var(--tone-violet) 100%);
    opacity: 0.8;
  }

  .title-disc {
    position: absolute;
    left: 410px; top: 245px; width: 410px; height: 410px;
    border-radius: 50%;
    background: var(--paper);
    display: flex; flex-direction: column; align-items: center; justify-content: center;
    text-align: center;
  }
  .title-kicker {
    font-weight: 800; font-size: 30px; letter-spacing: 6px;
    color: var(--accent-red); line-height: 1; margin-bottom: 8px;
    padding-left: 6px;
  }
  .title-main {
    font-weight: 300; font-size: 88px; line-height: 0.92;
    letter-spacing: 1px;
  }

  .author {
    position: absolute;
    top: 811px; left: 310px; width: 600px;
    text-align: center;
    font-size: 34px; font-weight: 500; letter-spacing: 11px;
    padding-left: 11px; white-space: nowrap;
  }
</style>
</head>
<body>
  <main class="cover">
    <span class="rule rule--top-a"></span>
    <p class="subtitle">A Week-by-Week Practical Workbook to Loosen Nervous Habits, Quieten Doubt and Build Steady Poise</p>
    <span class="rule rule--top-b"></span>

    <div class="artwork" role="img" aria-label="Cover artwork area: abstract multicoloured watercolour wash framing the title"></div>

    <h1 class="title-disc">
      <span class="title-kicker">QUIET ROOMS,</span>
      <span class="title-main">OPEN</span>
      <span class="title-main">DOORS</span>
    </h1>

    <span class="rule rule--bottom-a"></span>
    <p class="author">DR OWEN HARTLEY</p>
    <span class="rule rule--bottom-b"></span>
  </main>
</body>
</html>
```